Web site for Life Coaching Consultant

I require a website for a life coaching business. I have a Velvo Hosting account which I set up last week. I will need to be able to add articles and testimonials. The design should communicate that KT Amber Lantern is there to help people breakdown personal barriers and that we are an advocate to help them achieve personal goals.
Updates

Reason: I have some designers just accepting my invitation to submit so to give them a few days to submit. I have been thrilled with the quality of the submissions Thank you.

Hi everyone

I am loving all your designs.  The only feedback I can get from people is that they feel that the runner makes the web page look like a personal coach rather than a life coach that helps people with relations, career, and personal road blocks.

Sorry                                   

Reason: Hi I have increased the deadline as there has been so many amazing designs and some of you have asked to fine tune your entries. I would like to take this opportunity to thank you all. It is going to be a tough decision. I have put a few more pictures on the project page hoping this will help

Hi I just wanted to thank you all for your great designs.  As I got so many good designs I have asked people to vote.  I will be in touch in the next day or 2.

Cheers

Target Market(s)

People with self esteem issues either woman or girls, people who want to goal set and need an advocate

Industry/Entity Type

Life Coaching

Colors
d2a4cc
e567a6

Requirements
Must have
• must have bio section, logo, articles page, affirmation section and testimonial page.

```html
<!DOCTYPE html>
<html lang="en">
<head>
<meta charset="utf-8">
<title>KT Amber Lantern – Life Coaching</title>
<link href="https://fonts.googleapis.com/css2?family=Ubuntu:wght@400;500;700&family=Oswald:wght@600;700&display=swap" rel="stylesheet">
<style>
:root{
  --page-bg:#fbc3dc;
  --pink:#e91e7a;
  --magenta:#9b1553;
  --maroon:#8c1246;
  --orange:#f1a422;
  --orange-dark:#d88c12;
  --sky:#9fe6fa;
  --ink:#333;
  --plum:#8a1040;
  --white:#fff;
}
*{margin:0;padding:0;box-sizing:border-box}
html,body{width:853px;height:1200px;overflow:hidden}
body{background:var(--page-bg);font-family:"Ubuntu",sans-serif;color:var(--ink);position:relative}
.abs{position:absolute}
.top-social{left:702px;top:3px;display:flex;gap:3px}
.top-social span{width:16px;height:16px;border-radius:50%;display:block}
.fb{background:#3b5a9a}.tw{background:#2aa9e0}
.page{left:114px;top:23px;width:625px;height:1143px;background:var(--white);border-radius:6px 6px 0 0;overflow:hidden}
.nav{height:24px;background:var(--pink);display:flex;justify-content:center;align-items:center;gap:18px;font-size:10px;color:var(--white)}
.nav .active{font-weight:700}
.brand{left:0;top:24px;width:625px;height:103px;display:flex;align-items:center;justify-content:center;gap:14px}
.brand-dot{width:82px;height:82px;border-radius:50%;border:6px solid var(--pink);flex:none}
.brand-name{color:var(--pink);font-size:31px;font-weight:500;line-height:1}
.brand-tag{color:var(--pink);font-size:17px;margin-top:6px;text-align:center}
.hero{left:0;top:127px;width:625px;height:244px;background:var(--sky)}
.hero-photo{left:402px;top:0;width:223px;height:244px;background:linear-gradient(160deg,#b9dcea,#6b4a3a 55%,#2b2222)}
.hero h1{left:26px;top:54px;width:370px;font-family:"Oswald",sans-serif;font-weight:700;font-size:28px;line-height:38px;color:var(--plum);white-space:nowrap}
.hero h1 em{font-style:normal;color:var(--pink)}
.hero-sub{left:26px;top:135px;font-size:12px;color:#3a1d3a}
.hero-sub b{font-weight:700}
.cta{left:26px;top:172px;width:276px;height:29px;background:var(--orange);display:flex;align-items:center;color:var(--white);font-size:12px;white-space:nowrap}
.cta-play{width:43px;height:29px;background:var(--orange-dark);display:flex;align-items:center;justify-content:center;margin-right:9px;flex:none}
.intro{left:0;top:371px;width:625px;height:84px;background:var(--pink);overflow:hidden}
.intro-mark{left:10px;top:31px;color:var(--white);font-size:18px;font-weight:500;opacity:.9;white-space:nowrap}
.intro-circle{left:-30px;top:-10px;width:110px;height:110px;border-radius:50%;border:2px solid rgba(255,255,255,.25)}
.intro-rule{left:148px;top:8px;height:68px;border-left:1px dotted rgba(255,255,255,.7)}
.intro p{left:178px;top:12px;width:423px;font-size:9px;line-height:12px;color:var(--white)}
.feature{top:0;width:150px;text-align:center}
.feature-photo{width:110px;height:110px;border-radius:50%;margin:0 auto}
.feature h3{font-weight:400;font-size:12.5px;line-height:14px;margin-top:8px;color:var(--ink)}
.btn{display:inline-block;background:var(--orange);color:var(--white);font-size:9.5px;padding:5px 8px;margin-top:8px}
.features{left:0;top:500px;width:625px;height:230px}
.testimonial{left:0;top:727px;width:625px;height:103px;background:var(--magenta)}
.testimonial svg{position:absolute;left:0;top:0}
.testimonial h2{left:22px;top:34px;color:var(--white);font-weight:400;font-size:19px;letter-spacing:.5px}
.testimonial .more{left:22px;top:57px;color:var(--orange);font-size:8.5px;font-style:italic}
.t-photo{left:209px;top:7px;width:92px;height:92px;border-radius:50%;border:4px solid var(--white);background:linear-gradient(#d99a5a,#3a2620)}
.t-quote{left:326px;top:17px;width:272px;font-size:9px;line-height:11.5px;color:var(--white)}
.t-quote b{display:block;margin-top:10px;font-size:8.5px}
.articles h2{left:24px;top:865px;font-weight:400;font-size:20px;color:var(--plum)}
.article{top:902px;width:178px}
.article h4{font-size:9.5px;font-weight:700;color:var(--ink)}
.article time{display:block;font-size:9px;font-style:italic;color:var(--ink);margin-bottom:12px}
.article p{font-size:9px;line-height:12px;text-align:justify}
.article a{display:block;color:var(--orange);font-style:italic;font-size:9px;text-decoration:none;margin-top:2px}
.more-articles{left:542px;top:1031px;font-size:9px;font-style:italic;color:var(--plum)}
.footer{left:0;top:1057px;width:625px;height:86px;background:var(--pink);overflow:hidden}
.footer-left{left:0;top:0;width:228px;height:86px;background:var(--maroon)}
.footer-left h3{left:24px;top:22px;font-weight:400;font-size:16px;color:var(--white)}
.footer-left p{left:24px;top:42px;font-size:9.5px;line-height:11px;color:var(--white);white-space:nowrap}
.footer-left .addr{font-size:12px;line-height:14px}
.footer-links{top:18px;font-size:9px;line-height:16px;color:var(--white);list-style:none}
.footer-links .active{font-weight:700}
.footer-social{left:497px;top:28px;display:flex;gap:4px}
.footer-social span{width:34px;height:34px;border-radius:50%;display:block}
.footer-ring{left:572px;top:8px;width:80px;height:80px;border-radius:50%;border:2px solid rgba(255,255,255,.25)}
.copyright{left:0;top:1173px;width:853px;text-align:center;font-size:9px;color:var(--plum)}
</style>
</head>
<body>
<div class="abs top-social"><span class="fb"></span><span class="tw"></span></div>

<div class="abs page">
  <nav class="nav">
    <span>Home</span><span>Biography</span><span class="active">Special Offers</span><span>Articles</span><span>Affirmations</span><span>Testimonials</span>
  </nav>

  <header class="abs brand">
    <span class="brand-dot"></span>
    <div>
      <div class="brand-name">Amber Lantern</div>
      <div class="brand-tag">We help you get there</div>
    </div>
  </header>

  <section class="abs hero">
    <div class="abs hero-photo" role="img" aria-label="Photo of a smiling woman holding her glasses"></div>
    <h1 class="abs">OVERCOME <em>YOUR BOUNDARIES</em><br><em>EARN YOUR</em> HAPPINESS !</h1>
    <p class="abs hero-sub">Dare to <b>Dream Big</b>, <b>Set Goals</b>, and <b>TAKE ACTION !</b></p>
    <div class="abs cta">
      <span class="cta-play"><svg width="12" height="16" viewBox="0 0 12 16"><path d="M0 0L12 8L0 16Z" fill="#fff"/></svg></span>
      Follow our 10 steps Success Approach
    </div>
  </section>

  <section class="abs intro">
    <div class="abs intro-circle"></div>
    <div class="abs intro-mark">Amber Lantern</div>
    <div class="abs intro-rule"></div>
    <p class="abs">KT Amber Lantern is a <b>life coaching</b> group run by <b>Rachel Winslow</b>. Rachel, has 10 years as a Corporate Trainer specialized in team building, change management, negotiation skills, and sales and customers service. After leaving the corporate arena to have a family and assist her husband in his business ventures she has now returned to her passion of <b>assisting people to overcome boundaries and become who they would like to ultimately be.</b></p>
  </section>

  <section class="abs features">
    <div class="abs feature" style="left:86px">
      <div class="feature-photo" role="img" aria-label="Photo of a smiling couple" style="background:linear-gradient(135deg,#c9dce8,#e8c9a6 60%,#b68a6a)"></div>
      <h3>About<br>Rachel Winslow</h3>
      <span class="btn">Rachel's Biography</span>
    </div>
    <div class="abs feature" style="left:237px">
      <div class="feature-photo" role="img" aria-label="Photo of a confident woman silhouetted against the sky" style="background:linear-gradient(#b7b5d8,#7d6f8f 60%,#4a3a3e)"></div>
      <h3>I am STRONGER<br>than any excuse</h3>
      <span class="btn">More Affirmations</span>
    </div>
    <div class="abs feature" style="left:388px">
      <div class="feature-photo" role="img" aria-label="Photo of a smiling boy in a garden" style="background:linear-gradient(135deg,#6a8a3a,#d7c7b0 55%,#3a5a2a)"></div>
      <h3>Raise money for<br>Children’s Hospital</h3>
      <span class="btn">Special Offers</span>
    </div>
  </section>

  <section class="abs testimonial">
    <svg width="330" height="103" viewBox="0 0 330 103"><path d="M0 0H205L165 103H0Z" fill="#e91e7a"/></svg>
    <h2 class="abs">TESTIMONIAL</h2>
    <span class="abs more">more testimonials</span>
    <div class="abs t-photo" role="img" aria-label="Portrait photo of a client"></div>
    <p class="abs t-quote">Rachel help me through my boundaries, identifying what holds me back from moving on my current life. With her 10 Steps method, now I could reach most of my dreams and the best of it is I’m feeling much stronger and ready to reach all my goals.<b>- Maren</b></p>
  </section>

  <section class="articles">
    <h2 class="abs">Latest Articles</h2>
    <article class="abs article" style="left:26px">
      <h4>What is Life Coaching?</h4>
      <time>December 9, 2013</time>
      <p>Life Coaching helps individuals overcome road blocks in their lives which are usually due to relationship (family, friends or partner) breakdowns, career dissatisfaction or uncertainty of how to plan and implement personal goals.</p>
      <a>read more</a>
    </article>
    <article class="abs article" style="left:226px">
      <h4>We Help You To Get There</h4>
      <time>December 9, 2013</time>
      <p>We are currently looking for Pro bono clients, there will be no charge just if people are happy with the outcome I would be stoked if they would write a testimonial.</p>
      <a>read more</a>
    </article>
    <article class="abs article" style="left:426px">
      <h4>No, It’s Not a Secret . . .</h4>
      <time>December 9, 2013</time>
      <p>JOY attracts more joy, happiness attracts more happiness. Peace attracts more peace. So, to change your world, all you have to do is change the way you feel inside. How easy is that?</p>
      <a>read more</a>
    </article>
    <span class="abs more-articles">More Articles</span>
  </section>

  <footer class="abs footer">
    <div class="abs footer-left">
      <h3 class="abs">Rachel Winslow</h3>
      <p class="abs"><span class="addr">PO BOX 4152 Elwood VIC 3184</span><br>Mobile : 0400 555 123<br>Email : rachel@amberlantern.example</p>
    </div>
    <ul class="abs footer-links" style="left:263px">
      <li>Home</li><li>Biography</li><li class="active">Special Offers</li><li>Articles</li>
    </ul>
    <ul class="abs footer-links" style="left:367px">
      <li>Affirmations</li><li>Testimonials</li><li>Contact Us</li>
    </ul>
    <div class="abs footer-ring"></div>
    <div class="abs footer-social"><span class="fb"></span><span class="tw"></span></div>
  </footer>
</div>

<p class="abs copyright">Copyright © 2014 KTAmberLantern. All Rights Reserved.</p>
</body>
</html>
```